Website

I have a client that we built a website for about 10 years ago - https://www.pinloopcards.com.au/

We would like a fresh new design for it that looks more modern. All the elements, info that's on there needs to be the same but the whole design/layout needs to be modernised.

```html
<!DOCTYPE html>
<html lang="en">
<head>
<meta charset="utf-8">
<title>Pin Loop Cards – Promotional Button Badges</title>
<link href="https://fonts.googleapis.com/css2?family=Roboto:ital,wght@0,400;0,500;0,700;0,900;1,400&display=swap" rel="stylesheet">
<style>
:root{
  --red:#d10a11;
  --red-dark:#8e0508;
  --ink:#1f1f1f;
  --text:#444;
  --muted:#888;
  --grey:#ececec;
  --grey-mid:#d9d9d9;
  --dark:#2b2b2b;
  --white:#fff;
  --gold:#f0b400;
}
*{box-sizing:border-box;margin:0;padding:0}
html,body{width:1200px;height:5333px;overflow:hidden}
body{position:relative;background:var(--white);font-family:'Roboto',sans-serif;color:var(--ink)}
.abs{position:absolute}
.backdrop{position:absolute;left:0;top:0}
/* header */
.logo{left:145px;top:32px;display:flex;align-items:center;gap:12px}
.logo-mark{width:46px;height:46px;border-radius:50%;background:var(--red)}
.logo-name{font-size:30px;font-weight:900;color:var(--ink);letter-spacing:-.5px}
.pill{display:inline-flex;align-items:center;justify-content:center;gap:10px;border-radius:24px;color:var(--white);font-weight:700;font-size:13px;text-transform:uppercase;white-space:nowrap}
.pill .arrow{width:18px;height:18px;border-radius:50%;background:var(--white);display:inline-flex;align-items:center;justify-content:center}
.pill-dark{background:linear-gradient(#3a3a3a,#1e1e1e)}
.pill-red{background:linear-gradient(#e0161d,#b0070c)}
.pill-grey{background:linear-gradient(#8a8a8a,#5d5d5d)}
.nav{left:110px;top:130px;width:980px;height:52px;border-radius:26px;background:linear-gradient(90deg,#7d0306,var(--red) 50%,#7d0306);display:flex;align-items:center;padding:0 14px;gap:4px}
.nav a{color:var(--white);text-decoration:none;font-size:13px;font-weight:700;padding:12px 14px;border-radius:20px;text-transform:uppercase}
.nav a.active{background:#2a2a2a}
/* hero */
.dots{background-image:radial-gradient(circle,var(--red) 2px,transparent 2.5px);background-size:14px 14px}
.hero-title{left:141px;top:282px;font-size:54px;font-weight:700;line-height:60px;color:var(--ink)}
.hero-title em{font-style:normal;color:var(--red)}
.hero-lead{left:143px;top:488px;font-size:22px;line-height:34px;color:#333}
.hero-actions{left:143px;top:590px;display:flex;gap:10px}
.hero-actions .pill{height:44px;padding:0 16px}
.carousel-dots{left:143px;top:727px;display:flex;gap:15px}
.carousel-dots i{width:10px;height:10px;border-radius:50%;background:#aaa}
.carousel-dots i.on{background:var(--red)}
.photo{background:linear-gradient(160deg,#d8c4b3,#2d3442 60%,#1b2230)}
/* section titles */
.section-title{left:0;width:1200px;text-align:center;font-size:54px;font-weight:700;color:var(--ink)}
.section-title em{font-style:normal;color:var(--red)}
.section-title.light{color:var(--white)}
/* about */
.about-title{left:143px;top:922px;font-size:54px;font-weight:700}
.about-title em{font-style:normal;color:var(--red)}
.about-text{left:145px;top:1002px;width:450px;font-size:15.5px;line-height:29.6px;color:#444;text-align:justify}
.read-more{left:145px;top:1357px;height:44px;padding:0 20px}
.ring-big{left:697px;top:904px;width:372px;height:348px;border-radius:50%;background:var(--red);border:8px solid var(--white);box-shadow:0 0 0 4px var(--red)}
.ring-big .inner{position:absolute;inset:40px;border-radius:50%;background:linear-gradient(135deg,#f3c6a0,#e0212b 60%,#2b3a8f)}
.ring-small{left:645px;top:1148px;width:266px;height:276px;border-radius:50%;background:var(--white);border:5px solid #3a3a3a;padding:10px}
.ring-small .inner{width:100%;height:100%;border-radius:50%;background:linear-gradient(180deg,#efefef,#c9b8a8 45%,#3b3b3b)}
/* products */
.product{width:214px;height:214px;border-radius:50%;background:var(--white);box-shadow:0 6px 14px rgba(0,0,0,.18),inset 0 0 0 3px #e4e4e4;display:flex;flex-direction:column;align-items:center;padding-top:44px;text-align:center}
.product.featured{box-shadow:0 6px 14px rgba(0,0,0,.2),inset 0 0 0 8px var(--red)}
.product .thumb{width:92px;height:58px;border-radius:6px;background:linear-gradient(135deg,#d6d6d6,#9a9a9a)}
.product h3{margin-top:16px;font-size:14px;line-height:21px;font-weight:500;color:#333;width:140px}
.product .go{margin-top:10px;width:22px;height:22px;border-radius:50%;border:1.5px solid var(--red);display:flex;align-items:center;justify-content:center}
.view-more{height:44px;padding:0 20px}
/* why */
.feature{width:220px;text-align:center;color:var(--white)}
.feature .icon{margin:0 auto;width:90px;height:90px;border-radius:50%;background:#2c2c2c;box-shadow:0 0 0 6px rgba(255,255,255,.15),0 6px 12px rgba(0,0,0,.35);display:flex;align-items:center;justify-content:center}
.feature .icon.on{background:var(--red);box-shadow:0 0 0 6px #2c2c2c,0 6px 12px rgba(0,0,0,.35)}
.feature h3{margin-top:26px;font-size:16px;font-weight:700;line-height:23px;text-transform:uppercase}
.feature p{font-size:15px;line-height:23px}
/* testimonials */
.arrow-btn{width:42px;height:42px;border-radius:50%;border:2px solid #999;background:var(--white);display:flex;align-items:center;justify-content:center}
.testimonial{width:392px;height:188px;background:var(--white);border-radius:14px;box-shadow:0 4px 14px rgba(0,0,0,.15);border:2px solid #e8e8e8}
.testimonial .avatar{position:absolute;left:-28px;top:38px;width:92px;height:92px;border-radius:50%;border:4px solid var(--red);background:linear-gradient(160deg,#d9b49a,#3a2a24);box-shadow:0 0 0 4px var(--white)}
.testimonial blockquote{position:absolute;left:82px;top:22px;width:282px;font-size:13px;line-height:23px;font-style:italic;color:#555;text-align:justify}
.testimonial .who{position:absolute;left:82px;top:150px;font-size:13px;color:var(--red);display:flex;gap:16px;align-items:center}
.stars{color:var(--gold);letter-spacing:1px;font-size:14px}
/* news */
.news-card{width:274px;height:332px;background:var(--white);border-radius:6px;box-shadow:0 4px 12px rgba(0,0,0,.18);border:4px solid #e6e6e6;overflow:hidden}
.news-card .pic{height:150px;background:linear-gradient(135deg,#3b3b3b,#111)}
.news-card .pic.warm{background:linear-gradient(135deg,#c6a07c,#6d4c38)}
.news-card .date{position:absolute;left:18px;top:172px;width:44px;height:42px;background:var(--red);color:var(--white);text-align:center;font-size:19px;line-height:20px;padding-top:3px;font-weight:500}
.news-card .date small{display:block;font-size:12px;line-height:14px}
.news-card h3{position:absolute;left:76px;top:170px;width:180px;font-size:15px;line-height:22px;font-weight:500;color:#222}
.news-card p{position:absolute;left:18px;top:226px;width:236px;font-size:10.5px;line-height:17px;color:#888}
.news-card .more{position:absolute;left:18px;top:288px;font-size:12px;font-weight:700;color:var(--red)}
/* clients */
.client{width:213px;height:102px;background:var(--white);border:2px solid #d4d4d4;border-radius:4px;display:flex;align-items:center;justify-content:center;font-size:17px;font-weight:700;color:#333;gap:8px}
.client.hover{box-shadow:0 8px 14px rgba(209,10,17,.18)}
.client i{width:14px;height:14px;border-radius:50%;background:#333}
/* newsletter */
.newsletter{left:182px;top:4796px;width:834px;height:202px;background:linear-gradient(90deg,#c5070d,#e0141b,#b8060b);border-radius:24px;text-align:center}
.newsletter h2{margin-top:40px;font-size:33px;font-weight:700;color:var(--white)}
.newsletter form{position:absolute;left:63px;top:112px;display:flex;gap:10px}
.newsletter .field{width:274px;height:45px;border-radius:23px;background:var(--white);font-size:14px;color:#555;display:flex;align-items:center;padding-left:26px}
.newsletter .submit{width:140px;height:45px;border-radius:23px;background:#1e1e1e;color:var(--white);font-weight:700;font-size:14px;display:flex;align-items:center;justify-content:center}
/* footer */
.contact{display:flex;align-items:center;gap:16px;color:#ddd;font-size:13px;line-height:22px}
.contact .ci{width:40px;height:40px;border-radius:50%;border:2px solid #777;display:flex;align-items:center;justify-content:center}
.contact .ci.on{background:var(--red);border-color:var(--red)}
.footer-nav{left:0;width:1200px;top:5128px;display:flex;justify-content:center;gap:30px}
.footer-nav a{color:var(--white);font-size:13px;font-weight:500;text-decoration:none;text-transform:uppercase}
.legal{left:0;width:1200px;top:5180px;text-align:center;font-size:12px;color:#ccc}
.social{left:0;width:1200px;top:5240px;display:flex;justify-content:center;gap:8px}
.social span{height:26px;padding:0 10px;border-radius:13px;background:var(--white);color:#222;font-size:11px;font-weight:500;display:flex;align-items:center}
</style>
</head>
<body>

<svg class="backdrop" width="1200" height="5333" viewBox="0 0 1200 5333" aria-hidden="true">
  <defs>
    <linearGradient id="heroBg" x1="0" x2="1" y1="0" y2="0">
      <stop offset="0" stop-color="#e9e9e9"/><stop offset=".6" stop-color="#f4f4f4"/><stop offset="1" stop-color="#d8d8d8"/>
    </linearGradient>
    <linearGradient id="redBand" x1="0" x2="1" y1="0" y2="1">
      <stop offset="0" stop-color="#b5060b"/><stop offset=".5" stop-color="#dc0f16"/><stop offset="1" stop-color="#c0070d"/>
    </linearGradient>
  </defs>
  <!-- hero -->
  <path d="M0 157 H1200 V880 Q700 760 0 915 Z" fill="url(#heroBg)"/>
  <path d="M780 157 H1010 L1200 420 V640 Z" fill="#d70e15"/>
  <path d="M1040 157 H1120 L1200 270 V360 Z" fill="#a8060a"/>
  <path d="M0 915 Q700 760 1200 880" fill="none" stroke="#c70b12" stroke-width="4"/>
  <!-- products -->
  <path d="M0 1660 Q560 1380 1200 1490 V2300 C800 2430 300 2470 0 2330 Z" fill="var(--grey)"/>
  <path d="M0 1660 Q560 1380 1200 1490" fill="none" stroke="#c70b12" stroke-width="5"/>
  <!-- why choose us -->
  <path d="M0 2330 C300 2470 800 2430 1200 2300 V3040 C800 2900 300 2800 0 2890 Z" fill="url(#redBand)"/>
  <path d="M0 2330 C300 2470 800 2430 1200 2300" fill="none" stroke="#2a2a2a" stroke-width="6"/>
  <path d="M0 2890 C300 2800 800 2900 1200 3040" fill="none" stroke="#7d0306" stroke-width="4"/>
  <!-- news -->
  <path d="M0 3730 Q600 3530 1200 3615 V4330 Q600 4420 0 4230 Z" fill="var(--grey)"/>
  <path d="M0 3730 Q600 3530 1200 3615" fill="none" stroke="#c70b12" stroke-width="5"/>
  <path d="M0 4230 Q560 4440 1200 4320 Q560 4410 0 4250 Z" fill="#2a2a2a"/>
  <!-- footer -->
  <path d="M0 4775 Q600 4880 1200 4815 V5333 H0 Z" fill="var(--dark)"/>
  <path d="M0 4775 Q600 4880 1200 4815" fill="none" stroke="#c70b12" stroke-width="4"/>
</svg>

<!-- header -->
<header>
  <div class="abs logo"><span class="logo-mark"></span><span class="logo-name">Pin Loop Cards</span></div>
  <a class="abs pill pill-dark" style="left:592px;top:42px;width:198px;height:46px">Request a Quote <span class="arrow"><svg width="8" height="10" viewBox="0 0 8 10"><path d="M2 1l4 4-4 4" stroke="#222" stroke-width="2" fill="none"/></svg></span></a>
  <a class="abs pill pill-red" style="left:803px;top:42px;width:250px;height:46px">Order Your Badge Now <span class="arrow"><svg width="8" height="10" viewBox="0 0 8 10"><path d="M2 1l4 4-4 4" stroke="#c00" stroke-width="2" fill="none"/></svg></span></a>
  <nav class="abs nav">
    <a class="active">Home</a><a>Products</a><a>Price List</a><a>Re-Sellers Trade Info</a><a>Info</a><a>Artwork Requirements</a><a>Payment</a><a>Contact</a>
  </nav>
</header>

<!-- hero -->
<section>
  <div class="abs dots" style="left:24px;top:195px;width:70px;height:140px"></div>
  <div class="abs dots" style="left:24px;top:713px;width:70px;height:140px"></div>
  <div class="abs photo" role="img" aria-label="Smiling businessman in suit wearing a name badge" style="left:640px;top:200px;width:540px;height:660px;border-radius:260px 260px 0 0"></div>
  <h1 class="abs hero-title">Looking for a<br><em>Promotional</em><br>Button Badge?</h1>
  <p class="abs hero-lead">PLC will close over Christmas / New year.<br>We are back on 19th January 2025.</p>
  <div class="abs hero-actions">
    <a class="pill pill-red">Order Your Badge Now <span class="arrow"><svg width="8" height="10" viewBox="0 0 8 10"><path d="M2 1l4 4-4 4" stroke="#c00" stroke-width="2" fill="none"/></svg></span></a>
    <a class="pill pill-grey">Request a Quote <span class="arrow"><svg width="8" height="10" viewBox="0 0 8 10"><path d="M2 1l4 4-4 4" stroke="#555" stroke-width="2" fill="none"/></svg></span></a>
  </div>
  <div class="abs carousel-dots"><i></i><i class="on"></i><i></i></div>
</section>

<!-- about -->
<section>
  <h2 class="abs about-title">About <em>Us</em></h2>
  <p class="abs about-text">When it comes to name badges, tags, and other ID products, there's no service more trusted in Australia than Pin Loop Cards. True to our name, our name badges Australia company specialises in producing a wide range of high-quality identity tags and products, which you can customise to help make your company or event a success. Whether you're looking for top-notch IDs for your employees or a batch of promotional items for an upcoming event, we've got all your needs covered at Pin Loop Cards. The main highlight of our service is providing you the ability to take control of the look, feel, and finish of your name tags.</p>
  <a class="abs pill pill-red read-more">Read More <span class="arrow"><svg width="8" height="10" viewBox="0 0 8 10"><path d="M2 1l4 4-4 4" stroke="#c00" stroke-width="2" fill="none"/></svg></span></a>
  <div class="abs ring-big"><div class="inner" role="img" aria-label="Smiling woman presenting promotional button badges"></div></div>
  <div class="abs ring-small"><div class="inner" role="img" aria-label="Confident businesswoman with folded arms"></div></div>
</section>

<!-- products -->
<section>
  <h2 class="abs section-title" style="top:1642px">Our <em>Products</em></h2>
  <div class="abs product" style="left:152px;top:1765px"><div class="thumb" role="img" aria-label="Full colour name badge"></div><h3>Full Colour Name Badges</h3><span class="go"><svg width="8" height="10" viewBox="0 0 8 10"><path d="M2 1l4 4-4 4" stroke="#d10a11" stroke-width="1.6" fill="none"/></svg></span></div>
  <div class="abs product featured" style="left:379px;top:1765px"><div class="thumb" role="img" aria-label="Round button badge" style="width:62px;height:62px;border-radius:50%"></div><h3>Button Badges</h3><span class="go"><svg width="8" height="10" viewBox="0 0 8 10"><path d="M2 1l4 4-4 4" stroke="#d10a11" stroke-width="1.6" fill="none"/></svg></span></div>
  <div class="abs product" style="left:607px;top:1765px"><div class="thumb" role="img" aria-label="Reusable name badge"></div><h3>Reusable Name Badges</h3><span class="go"><svg width="8" height="10" viewBox="0 0 8 10"><path d="M2 1l4 4-4 4" stroke="#d10a11" stroke-width="1.6" fill="none"/></svg></span></div>
  <div class="abs product" style="left:834px;top:1765px"><div class="thumb" role="img" aria-label="Engraved name badge"></div><h3>Engraved Name Badges</h3><span class="go"><svg width="8" height="10" viewBox="0 0 8 10"><path d="M2 1l4 4-4 4" stroke="#d10a11" stroke-width="1.6" fill="none"/></svg></span></div>
  <div class="abs product" style="left:152px;top:1999px"><div class="thumb" role="img" aria-label="Photo ID card"></div><h3>Photo ID Card / ID Card</h3><span class="go"><svg width="8" height="10" viewBox="0 0 8 10"><path d="M2 1l4 4-4 4" stroke="#d10a11" stroke-width="1.6" fill="none"/></svg></span></div>
  <div class="abs product" style="left:379px;top:1999px"><div class="thumb" role="img" aria-label="Membership card" style="background:linear-gradient(135deg,#222,#000)"></div><h3>Membership / Gift / Loyalty / VIP Cards</h3><span class="go"><svg width="8" height="10" viewBox="0 0 8 10"><path d="M2 1l4 4-4 4" stroke="#d10a11" stroke-width="1.6" fill="none"/></svg></span></div>
  <div class="abs product" style="left:607px;top:1999px"><div class="thumb" role="img" aria-label="Enamel lapel pin" style="width:62px;height:62px;border-radius:50%;background:linear-gradient(135deg,#e0b84a,#8a5a10)"></div><h3>Lapel Pins</h3><span class="go"><svg width="8" height="10" viewBox="0 0 8 10"><path d="M2 1l4 4-4 4" stroke="#d10a11" stroke-width="1.6" fill="none"/></svg></span></div>
  <div class="abs product" style="left:834px;top:1999px"><div class="thumb" role="img" aria-label="Black lanyard" style="height:40px;background:linear-gradient(90deg,#111,#555)"></div><h3>Lanyards</h3><span class="go"><svg width="8" height="10" viewBox="0 0 8 10"><path d="M2 1l4 4-4 4" stroke="#d10a11" stroke-width="1.6" fill="none"/></svg></span></div>
  <a class="abs pill pill-red view-more" style="left:515px;top:2270px">View More <span class="arrow"><svg width="8" height="10" viewBox="0 0 8 10"><path d="M2 1l4 4-4 4" stroke="#c00" stroke-width="2" fill="none"/></svg></span></a>
</section>

<!-- why choose us -->
<section>
  <h2 class="abs section-title light" style="top:2563px">Why Choose Us</h2>
  <svg class="abs" style="left:265px;top:2726px" width="666" height="4" aria-hidden="true"><line x1="0" y1="2" x2="666" y2="2" stroke="#8e0508" stroke-width="3"/></svg>
  <div class="abs feature" style="left:155px;top:2682px"><div class="icon on"><svg width="34" height="34" viewBox="0 0 24 24"><path d="M3 12V4h8l10 10-8 8z" fill="#fff"/><circle cx="7.5" cy="8" r="1.6" fill="#d10a11"/></svg></div><h3>No Minimum<br>Order</h3><p>on name badges</p></div>
  <div class="abs feature" style="left:378px;top:2682px"><div class="icon"><svg width="36" height="30" viewBox="0 0 24 20"><path d="M1 3h13v11H1zM14 7h5l4 4v3h-9z" fill="#fff"/><circle cx="6" cy="16" r="2.4" fill="#fff" stroke="#2c2c2c"/><circle cx="18" cy="16" r="2.4" fill="#fff" stroke="#2c2c2c"/></svg></div><h3>Fast<br>Delivery</h3></div>
  <div class="abs feature" style="left:600px;top:2682px"><div class="icon"><svg width="32" height="32" viewBox="0 0 24 24"><circle cx="12" cy="12" r="7" fill="none" stroke="#fff" stroke-width="4" stroke-dasharray="3.2 2.3"/><circle cx="12" cy="12" r="5" fill="#fff"/><circle cx="12" cy="12" r="2.2" fill="#2c2c2c"/></svg></div><h3>Free Setup</h3></div>
  <div class="abs feature" style="left:821px;top:2682px"><div class="icon"><span style="color:#fff;font-size:32px;font-weight:700">$</span></div><h3>Free Postage*</h3><p>For badge orders<br>over $400</p></div>
</section>

<!-- testimonials -->
<section>
  <h2 class="abs section-title" style="top:3136px">Customer <em>Testimonials</em></h2>
  <div class="abs arrow-btn" style="left:93px;top:3341px"><svg width="10" height="14" viewBox="0 0 10 14"><path d="M8 1L2 7l6 6" stroke="#777" stroke-width="2" fill="none"/></svg></div>
  <div class="abs arrow-btn" style="left:1064px;top:3341px"><svg width="10" height="14" viewBox="0 0 10 14"><path d="M2 1l6 6-6 6" stroke="#777" stroke-width="2" fill="none"/></svg></div>
  <div class="abs testimonial" style="left:194px;top:3268px">
    <span class="avatar" role="img" aria-label="Customer portrait"></span>
    <blockquote>"Thank you so much for the wonderful job you have done on our name badges for Glow Skin Studio. You have great attention to detail as they are an exact match to our colours and logo."</blockquote>
    <div class="who">Glow Skin Studio Southport <span class="stars">★★★★★</span></div>
  </div>
  <div class="abs testimonial" style="left:641px;top:3268px">
    <span class="avatar" role="img" aria-label="Customer portrait"></span>
    <blockquote>"I also wanted to sincerely thank you for providing such quality to PLC. We have had several rounds of trouble getting these badges right from other suppliers, so I was very pleased"</blockquote>
    <div class="who">Marlena, Ipswich <span class="stars">★★★★★</span></div>
  </div>
</section>

<!-- news -->
<section>
  <h2 class="abs section-title" style="top:3702px">Latest <em>News</em></h2>
  <article class="abs news-card" style="left:166px;top:3812px"><div class="pic" role="img" aria-label="Round blue club button badge"></div><div class="date">02<small>JAN</small></div><h3>Pellentesque faucibus Ut accumsan ultric</h3><p>Duis quam Nam eget lacus Aliquam erat volutpat Quisque dignissim congue leo Mauris vel lacus vitae felis vestibulum</p><span class="more">READ MORE</span></article>
  <article class="abs news-card" style="left:463px;top:3812px"><div class="pic warm" role="img" aria-label="Woman holding up a staff ID card"></div><div class="date">02<small>JAN</small></div><h3>Pellentesque faucibus Ut accumsan ultric</h3><p>Duis quam Nam eget lacus Aliquam erat volutpat Quisque dignissim congue leo Mauris vel lacus vitae felis vestibulum</p><span class="more">READ MORE</span></article>
  <article class="abs news-card" style="left:761px;top:3812px"><div class="pic" role="img" aria-label="Metal dog tag on a chain"></div><div class="date">02<small>JAN</small></div><h3>Pellentesque faucibus Ut accumsan ultric</h3><p>Duis quam Nam eget lacus Aliquam erat volutpat Quisque dignissim congue leo Mauris vel lacus vitae felis vestibulum</p><span class="more">READ MORE</span></article>
  <a class="abs pill pill-red view-more" style="left:515px;top:4188px">View More <span class="arrow"><svg width="8" height="10" viewBox="0 0 8 10"><path d="M2 1l4 4-4 4" stroke="#c00" stroke-width="2" fill="none"/></svg></span></a>
</section>

<!-- clients -->
<section>
  <h2 class="abs section-title" style="top:4484px">Our <em>Clients</em></h2>
  <div class="abs arrow-btn" style="left:93px;top:4631px"><svg width="10" height="14" viewBox="0 0 10 14"><path d="M8 1L2 7l6 6" stroke="#777" stroke-width="2" fill="none"/></svg></div>
  <div class="abs arrow-btn" style="left:1064px;top:4631px"><svg width="10" height="14" viewBox="0 0 10 14"><path d="M2 1l6 6-6 6" stroke="#777" stroke-width="2" fill="none"/></svg></div>
  <div class="abs client" style="left:145px;top:4601px"><i></i>Harbourview Golf</div>
  <div class="abs client hover" style="left:377px;top:4601px">Tidewell Aid</div>
  <div class="abs client" style="left:608px;top:4601px"><i></i>Larkspur Hotels</div>
  <div class="abs client" style="left:842px;top:4601px">Stride Staffing</div>
</section>

<!-- newsletter -->
<section class="abs newsletter">
  <h2>Sign Up to Newsletter</h2>
  <form>
    <span class="field">Enter Name</span>
    <span class="field">Enter Email</span>
    <span class="submit">SUBSCRIBE</span>
  </form>
</section>

<!-- footer -->
<footer>
  <div class="abs contact" style="left:240px;top:5052px"><span class="ci"><svg width="14" height="18" viewBox="0 0 14 18"><path d="M7 1a6 6 0 0 1 6 6c0 4-6 10-6 10S1 11 1 7a6 6 0 0 1 6-6z" fill="none" stroke="#ddd" stroke-width="1.6"/><circle cx="7" cy="7" r="2" fill="#ddd"/></svg></span><span>Postal: PO Box 4082,<br>Kensington Rise QLD 4352</span></div>
  <div class="abs contact" style="left:524px;top:5052px"><span class="ci on"><svg width="16" height="16" viewBox="0 0 24 24"><path d="M6.6 10.8a15 15 0 0 0 6.6 6.6l2.2-2.2c.3-.3.7-.4 1-.2 1.1.4 2.3.6 3.6.6.6 0 1 .4 1 1V20c0 .6-.4 1-1 1A17 17 0 0 1 3 4c0-.6.4-1 1-1h3.5c.6 0 1 .4 1 1 0 1.3.2 2.5.6 3.6.1.3 0 .7-.2 1z" fill="#fff"/></svg></span><span>Phone: 1300 555 214</span></div>
  <div class="abs contact" style="left:755px;top:5052px"><span class="ci"><svg width="18" height="16" viewBox="0 0 18 16"><rect x="4" y="1" width="10" height="5" fill="none" stroke="#ddd" stroke-width="1.5"/><rect x="1" y="6" width="16" height="9" rx="2" fill="#ddd"/></svg></span><span>Fax: 07 5550 1932</span></div>
  <nav class="abs footer-nav"><a>Home</a><a>Products</a><a>Price List</a><a>Re-Sellers Trade Info</a><a>Info</a><a>Artwork Requirements</a><a>Payment</a><a>Contact</a></nav>
  <p class="abs legal">©. Copyright 2026. Pin Loop Cards. All rights reserved &nbsp;|&nbsp; Privacy Policy &nbsp;|&nbsp; Terms of use</p>
  <div class="abs social"><span>Gallery</span><span>Community</span><span>Updates</span><span>Videos</span><span>Network</span></div>
</footer>

</body>
</html>
```